We need to redesign the packaging we use for our tempered glass screen protectors. The packaging needs to be modern and up to date as we feel our current packaging is outdated and we want to stand out from the competition. We would like to use a blue packaging colour with a modern twist. Our new Logo is named Vorn so this should be around the top of the packaging. We will need to use this packaging for on our different models of phones so it is not possible to attach a photo of a phone so any ideas will be appreciated. At the back of the packaging we would like the installation guide. A would prefer a better layout.

Target Market(s)

This product will target the 20s - 30s market.

Requirements
Must have
• Attached is our "Vorn Logo" which is on a laptop adapter box, please cut this out and use it on our Vorn Tempered Glass Screen Protector Packaging Design. Also there is an Example of Template which is the actual size of the packaging.
Nice to have
• Attached is the Palubo Packaging, we like the colour scheme.

```html
<!DOCTYPE html>
<html lang="en">
<head>
<meta charset="utf-8">
<title>Vorn Tempered Glass Screen Protector</title>
<link rel="stylesheet" href="https://fonts.googleapis.com/css2?family=Saira+Condensed:wght@300;400;600;700&display=swap">
<style>
  :root {
    --stage: #3b4250;
    --pack-deep: #0b1f66;
    --pack-mid: #0b3c9e;
    --pack-glow: #0a84d6;
    --gold: #f7aa1c;
    --white: #ffffff;
    --ice: #a9c8f2;
    --line: rgba(200, 220, 255, 0.75);
  }
  * { margin: 0; padding: 0; box-sizing: border-box; }
  html, body { width: 1200px; height: 1200px; overflow: hidden; }
  body {
    background: var(--stage);
    font-family: "Saira Condensed", sans-serif;
    position: relative;
  }
  .package {
    position: absolute;
    left: 326px; top: 96px;
    width: 567px; height: 988px;
    overflow: hidden;
    background: linear-gradient(180deg, var(--pack-deep) 0%, var(--pack-mid) 45%, #0a3a98 100%);
  }
  .product-visual {
    position: absolute;
    left: 0; top: 420px;
    width: 567px; height: 540px;
    background: radial-gradient(ellipse 60% 50% at 35% 45%, rgba(150, 205, 245, 0.75) 0%, rgba(10, 132, 214, 0.55) 40%, rgba(11, 60, 158, 0) 80%);
  }
  .brand {
    position: absolute;
    left: 360px; top: 52px; width: 144px; height: 48px;
    display: flex; align-items: center; justify-content: center; gap: 10px;
  }
  .brand-dot {
    width: 28px; height: 28px; border-radius: 50%;
    background: var(--white);
  }
  .brand-name {
    font-size: 36px; font-weight: 600; color: var(--white); line-height: 1;
  }
  .title {
    position: absolute; right: 62px;
    color: var(--gold);
    font-weight: 400;
    line-height: 1;
    text-shadow: 2px 3px 0 rgba(5, 20, 70, 0.7);
  }
  .title-tempered { top: 126px; font-size: 106px; letter-spacing: 1px; }
  .title-glass { top: 230px; font-size: 106px; letter-spacing: 1px; }
  .subtitle {
    position: absolute; right: 62px; top: 340px;
    font-size: 34px; font-weight: 700; color: var(--white); line-height: 1;
  }
  .hardness-badge {
    position: absolute; left: 114px; top: 243px;
    width: 135px; height: 127px;
    border: 2px solid rgba(120, 160, 230, 0.8);
    border-radius: 8px;
    background: rgba(40, 80, 170, 0.35);
    text-align: center;
  }
  .hardness-value {
    display: block; margin-top: 4px;
    font-size: 84px; font-weight: 300; line-height: 1;
    color: var(--pack-deep);
    -webkit-text-stroke: 1.5px var(--ice);
  }
  .hardness-label {
    display: block; margin-top: 4px;
    font-size: 14px; font-weight: 400; color: var(--ice); letter-spacing: 0.5px;
  }
  .features {
    position: absolute; left: 0; top: 0; width: 100%; list-style: none;
  }
  .features li {
    position: absolute;
    font-size: 25px; font-weight: 400; color: var(--white); line-height: 1;
    white-space: nowrap;
  }
  .features li:nth-child(1) { right: 53px;  top: 694px; }
  .features li:nth-child(2) { right: 93px;  top: 735px; }
  .features li:nth-child(3) { right: 111px; top: 775px; }
  .features li:nth-child(4) { right: 146px; top: 816px; }
  .model-tag {
    position: absolute; left: 244px; top: 875px;
    width: 260px; height: 71px;
    border: 2px solid var(--line); border-radius: 10px;
  }
  .model-tag::before {
    content: ""; position: absolute; left: 16px; right: 16px; top: 9px; bottom: 9px;
    border: 1px solid rgba(200, 220, 255, 0.5);
  }
  .model-name {
    position: absolute; inset: 0;
    display: flex; align-items: center; justify-content: center;
    font-size: 30px; font-weight: 600; color: var(--white);
  }
</style>
</head>
<body>
  <main class="package">
    <div class="product-visual" role="img" aria-label="Illustration of a clear tempered glass screen protector"></div>

    <div class="brand">
      <span class="brand-dot"></span>
      <span class="brand-name">Vorn</span>
    </div>

    <h1>
      <span class="title title-tempered">TEMPERED</span>
      <span class="title title-glass">GLASS</span>
    </h1>
    <p class="subtitle">SCREEN PROTECTOR</p>

    <div class="hardness-badge">
      <span class="hardness-value">9H</span>
      <span class="hardness-label">SUPER HARDNESS</span>
    </div>

    <ul class="features">
      <li>Delicate Touch</li>
      <li>Explosion Proof</li>
      <li>HD Transmittance</li>
      <li>Oleophobic Coated</li>
    </ul>

    <div class="model-tag">
      <span class="model-name">For Lumo 6s</span>
    </div>
  </main>
</body>
</html>
```